Dental Lab Delivery Box Design 163x115x97mm

* AI file of the box attached
* Full-Color outside and one color inside
* Return pictures of the 3D design; so we can have a better idea of how it will turn out
* Match Logo Color and Design
* Please find attached Words doc for the wording
* Research the dental lab delivery
* Attached our sister lab dental lab design
*
Updates

Target Market(s)

Dental Office

Industry/Entity Type

Dental Lab

Font styles to use
Serif

Colors
0054AA
0677BA
7BADD7
CADEEF
E8F1F8

Requirements
Must have
• Advance, Clean, and Matched Logo color
Nice to have
• Graphics
Should not have
• Too much words or over advertise

```html
<!DOCTYPE html>
<html lang="en">
<head>
<meta charset="utf-8">
<title>Velora Dental Inc — Delivery Box Dielines</title>
<link href="https://fonts.googleapis.com/css2?family=Jost:wght@400;600&display=swap" rel="stylesheet">
<style>
  :root {
    --backdrop: #cce4f3;
    --box-blue: #55aadb;
    --brand-navy: #0054aa;
    --brand-blue: #0677ba;
    --brand-sky: #7badd7;
    --brand-mist: #e8f1f8;
    --panel-white: #ffffff;
    --fold-line: #9fcbe9;
    --cut-line: #b98fd6;
  }
  html, body {
    margin: 0;
    padding: 0;
    width: 1200px;
    height: 1200px;
    overflow: hidden;
    background: var(--backdrop);
  }
  .canvas { display: block; width: 1200px; height: 1200px; }
  .panel-blue { fill: var(--box-blue); }
  .panel-white { fill: var(--panel-white); }
  .cut { stroke: var(--cut-line); stroke-width: 1.2; }
  .fold { stroke: var(--fold-line); stroke-width: 1.2; fill: none; }
  .fold-light { stroke: #cfe6f5; stroke-width: 1.4; fill: none; }
  .brand-name { font-family: "Jost", sans-serif; font-weight: 600; fill: var(--brand-navy); }
  .brand-name.on-blue { fill: var(--panel-white); }
  .brand-dot { fill: var(--brand-navy); }
  .brand-dot.on-blue { fill: var(--panel-white); }
  .tagline { font-family: "Jost", sans-serif; font-weight: 400; font-size: 17px; fill: var(--brand-blue); }
  .tagline.on-blue { fill: var(--panel-white); }
  .tagline.on-band { fill: var(--panel-white); font-size: 14px; }
  .welcome-copy { font-family: "Jost", sans-serif; font-size: 10.5px; fill: #5a6a78; }
  .address-hint { font-family: "Jost", sans-serif; font-size: 17px; fill: #dbe9f4; }
</style>
</head>
<body>
<svg class="canvas" viewBox="14 -430 1904 1904" xmlns="http://www.w3.org/2000/svg" aria-label="Velora Dental Inc mailer box dielines, outside and inside">
  <defs>
    <radialGradient id="lidGlow" cx="50%" cy="48%" r="55%">
      <stop offset="0%" stop-color="#ffffff"/>
      <stop offset="45%" stop-color="#ffffff"/>
      <stop offset="100%" stop-color="#55aadb"/>
    </radialGradient>
    <linearGradient id="swooshTop" x1="1" y1="0" x2="0" y2="1">
      <stop offset="0%" stop-color="#7badd7" stop-opacity="0.55"/>
      <stop offset="60%" stop-color="#7badd7" stop-opacity="0"/>
    </linearGradient>
    <linearGradient id="swooshBottom" x1="0" y1="1" x2="1" y2="0">
      <stop offset="0%" stop-color="#7badd7" stop-opacity="0.55"/>
      <stop offset="60%" stop-color="#7badd7" stop-opacity="0"/>
    </linearGradient>
  </defs>

  <!-- ============ OUTSIDE DIELINE ============ -->
  <g class="dieline-outside">
    <!-- back closing flap -->
    <g class="back-flap">
      <polygon class="panel-blue cut" points="300,55 397,55 397,225 362,225 300,208"/>
      <rect class="panel-blue cut" x="397" y="55" width="303" height="170"/>
      <polygon class="panel-blue cut" points="700,55 797,55 797,208 735,225 700,225"/>
      <line class="fold" x1="397" y1="55" x2="397" y2="225"/>
      <line class="fold" x1="700" y1="55" x2="700" y2="225"/>
    </g>

    <!-- lid row -->
    <g class="lid-row">
      <polygon class="panel-blue cut" points="36,232 208,232 208,430 36,430 36,375 30,375 30,290 36,290"/>
      <polygon class="panel-blue cut" points="208,232 216,227 216,437 208,430"/>
      <rect class="panel-white cut" x="216" y="227" width="175" height="210"/>
      <rect class="cut" x="391" y="227" width="315" height="210" fill="url(#lidGlow)"/>
      <rect class="panel-white cut" x="706" y="227" width="176" height="210"/>
      <polygon class="panel-blue cut" points="882,227 890,232 890,430 882,437"/>
      <polygon class="panel-blue cut" points="890,232 1061,232 1061,290 1067,290 1067,375 1061,375 1061,430 890,430"/>

      <g class="side-panel-left" transform="translate(300,332) rotate(-90)">
        <circle class="brand-dot" cx="-70" cy="0" r="6"/>
        <text class="brand-name" x="10" y="6" font-size="18" text-anchor="middle">Velora Dental Inc</text>
      </g>
      <g class="lid-brand">
        <circle class="brand-dot" cx="443" cy="331" r="9"/>
        <text class="brand-name" x="558" y="340" font-size="26" text-anchor="middle">Velora Dental Inc</text>
        <text class="tagline" x="548" y="382" text-anchor="middle">Every Detail Matters</text>
      </g>
      <g class="side-panel-right" transform="translate(797,332) rotate(90)">
        <circle class="brand-dot" cx="-70" cy="0" r="6"/>
        <text class="brand-name" x="10" y="6" font-size="18" text-anchor="middle">Velora Dental Inc</text>
      </g>
    </g>

    <!-- inner front panel (printed welcome) -->
    <g class="welcome-row">
      <polygon class="panel-white cut" points="300,455 332,440 397,440 397,610 300,610"/>
      <rect class="panel-white cut" x="397" y="440" width="303" height="172"/>
      <polygon class="panel-white cut" points="700,440 765,440 797,455 797,610 700,610"/>
      <g transform="rotate(180 548 526)">
        <circle class="brand-dot" cx="424" cy="475" r="4"/>
        <text class="brand-name" x="431" y="479" font-size="12">Velora Dental Inc</text>
        <text class="welcome-copy" x="420" y="500">Welcome to Velora! Headquartered in Riverside Falls, we</text>
        <text class="welcome-copy" x="420" y="512">are a full digital dental lab for all you need. We strive to build</text>
        <text class="welcome-copy" x="420" y="524">excellent relationship and services with our clients, utilize highly</text>
        <text class="welcome-copy" x="420" y="536">experienced technicians and advance case management systems.</text>
        <text class="welcome-copy" x="420" y="548">Velora stands for Vision, Excellence, Loyalty, Reach. We care for your</text>
        <text class="welcome-copy" x="420" y="560">team as one team.</text>
        <text class="welcome-copy" x="420" y="578">Velora looks forward to building and improving your reputation and</text>
        <text class="welcome-copy" x="420" y="590">bringing more smiles to our services.</text>
      </g>
    </g>

    <!-- base top panel with large brand -->
    <g class="base-row">
      <path class="panel-blue cut" d="M402,614 L402,826 L270,795 Q228,785 228,745 L228,690 Q228,652 270,642 Z"/>
      <rect class="panel-white cut" x="402" y="612" width="294" height="214"/>
      <path class="panel-blue cut" d="M696,614 L830,642 Q871,652 871,690 L871,745 Q871,785 830,795 L696,826 Z"/>
      <rect x="560" y="614" width="136" height="110" fill="url(#swooshTop)" role="img" aria-label="Fine sweeping line graphic in light blue"/>
      <rect x="402" y="716" width="136" height="110" fill="url(#swooshBottom)" role="img" aria-label="Fine sweeping line graphic in light blue"/>
      <circle class="brand-dot" cx="443" cy="716" r="9"/>
      <text class="brand-name" x="558" y="725" font-size="26" text-anchor="middle">Velora Dental Inc</text>
    </g>

    <!-- bottom panel with address space -->
    <g class="address-row">
      <path class="panel-blue cut" d="M395,838 L395,1000 L330,1000 Q240,990 232,910 L232,838 Z"/>
      <rect class="panel-white cut" x="395" y="826" width="308" height="174"/>
      <path class="panel-blue cut" d="M703,838 L866,838 L866,880 Q860,990 770,1000 L703,1000 Z"/>
      <rect x="470" y="852" width="156" height="74" fill="var(--brand-mist)" opacity="0.6"/>
      <text class="address-hint" x="548" y="898" text-anchor="middle" transform="rotate(-15 548 893)">Space for Address:</text>
      <rect x="496" y="970" width="207" height="16" fill="var(--box-blue)"/>
      <text class="tagline on-band" x="622" y="983" text-anchor="middle">Every Detail Matters</text>
      <circle class="brand-dot" cx="425" cy="976" r="3.5"/>
      <text class="brand-name" x="431" y="979" font-size="7.5">Velora Dental Inc</text>
    </g>
  </g>

  <!-- ============ INSIDE DIELINE (one colour) ============ -->
  <g class="dieline-inside" role="img" aria-label="Inside print, solid blue with faint repeating small tooth pattern">
    <!-- lid closing flap -->
    <path class="panel-blue" d="M1175,52 L1655,52 Q1710,60 1715,140 Q1715,195 1690,208 L1557,208 L1550,218 L1270,218 L1265,208 L1140,208 Q1107,205 1107,175 Q1110,80 1175,52 Z"/>
    <line class="fold-light" x1="1265" y1="52" x2="1265" y2="218"/>
    <line class="fold-light" x1="1557" y1="52" x2="1557" y2="218"/>

    <!-- lid inside -->
    <path class="panel-blue" d="M1270,220 L1270,423 L1135,390 Q1103,382 1103,350 L1103,290 Q1103,262 1135,255 Z"/>
    <rect class="panel-blue" x="1270" y="218" width="280" height="205"/>
    <path class="panel-blue" d="M1550,220 L1688,255 Q1718,262 1718,290 L1718,350 Q1718,382 1688,390 L1550,423 Z"/>
    <line class="fold-light" x1="1270" y1="218" x2="1270" y2="423"/>
    <line class="fold-light" x1="1550" y1="218" x2="1550" y2="423"/>
    <circle class="brand-dot on-blue" cx="1322" cy="315" r="7"/>
    <text class="brand-name on-blue" x="1418" y="322" font-size="21" text-anchor="middle">Velora Dental Inc</text>
    <text class="tagline on-blue" x="1411" y="364" text-anchor="middle" font-size="15">Every Detail Matters</text>

    <!-- back wall -->
    <polygon class="panel-blue" points="1173,427 1265,427 1265,590 1210,590 1173,572"/>
    <rect class="panel-blue" x="1265" y="425" width="292" height="165"/>
    <polygon class="panel-blue" points="1557,427 1648,427 1648,572 1612,590 1557,590"/>
    <line class="fold-light" x1="1265" y1="425" x2="1265" y2="590"/>
    <line class="fold-light" x1="1557" y1="425" x2="1557" y2="590"/>

    <!-- base row -->
    <polygon class="panel-blue" points="922,596 1085,596 1085,786 922,786 922,740 915,740 915,650 922,650"/>
    <rect class="panel-blue" x="1093" y="591" width="169" height="200"/>
    <rect class="panel-blue" x="1262" y="590" width="298" height="200"/>
    <rect class="panel-blue" x="1560" y="591" width="170" height="200"/>
    <polygon class="panel-blue" points="1737,596 1900,596 1900,650 1906,650 1906,740 1900,740 1900,786 1737,786"/>
    <line class="fold-light" x1="1089" y1="596" x2="1089" y2="786"/>
    <line class="fold-light" x1="1262" y1="590" x2="1262" y2="790"/>
    <line class="fold-light" x1="1560" y1="590" x2="1560" y2="790"/>
    <line class="fold-light" x1="1733" y1="596" x2="1733" y2="786"/>
    <line class="fold-light" x1="1262" y1="590" x2="1560" y2="590"/>
    <line class="fold-light" x1="1262" y1="790" x2="1560" y2="790"/>

    <!-- front wall -->
    <polygon class="panel-blue" points="1210,795 1265,795 1265,955 1173,955 1173,812"/>
    <rect class="panel-blue" x="1265" y="792" width="292" height="163"/>
    <polygon class="panel-blue" points="1557,795 1612,795 1648,812 1648,955 1557,955"/>
    <line class="fold-light" x1="1265" y1="795" x2="1265" y2="955"/>
    <line class="fold-light" x1="1557" y1="795" x2="1557" y2="955"/>
  </g>
</svg>
</body>
</html>
```